A poster for Vale Chiropractic's up coming powerful health workshop/seminar

I need a poster developed for Dr. Prent's upcoming Total Shape Reset and Armor Plating your Wellness seminar/workshop. This workshop will teach attendants how to shed pounds and rapidly reduce their waist size. Learn why weight loss doesn't work 99.9% of the time so that you can be the successful .1%. It's time to expose the LIES and reveal the TRUTH about the REAL causes of HEART DISEASE, DIABETES, CANCER, CHRONIC FATIGUE, ARTHRITIS, FIBROMYALGIA, and how to REVERSE/PREVENT this from ever happening to you or your family. The Insider Secrets to building your body into a health fortress unbreachable by sickness and disease. Learn to live and fufill your GOD-GIVEN health potential. Eliminate high bloodpressure, high cholesterol, diabetes, fatigue, chronic pain
Ending the WAR on sickness and disease by launching an unstoppable health offensive that will pummel any enemy of life and health.

I'm not a designer by any means, but was thinking of possible WAR theme, cammo, etc....just a thought. Not a requirement by any means
Updates

Dr. Prent has taken a look at all the submissions and has requested a few changes.

1. He wants the new map that has been added to the brief with Marlow Ridge College as a title above the map

2. He wants a section that describes what the attendees will gain at the seminar in bullet format.  Example:  Title....It's not about what you lose

                                                   I'ts about what you gain....

>The No-Hype, No- Gimmick  secrets for fast effective Weight loss

>How the top 3 disease killers, heart disease, cancer, and diabetes are linked to diet

>Tools and strategies to make 2012 the best year ever

The Seminar will be held at Marlow Ridge College, Tuesday January 3rd @ 6:30pm Open to Public

Target Market(s)

Adults 30-65

Industry/Entity Type

Building

Requirements
Should not have
• ruyrtur

```html
<!DOCTYPE html>
<html lang="en">
<head>
<meta charset="utf-8">
<title>Dr. Prent's Seminar – Total Shape Reset and Armor Plating your Wellness</title>
<link rel="stylesheet" href="https://fonts.googleapis.com/css2?family=Stardos+Stencil:wght@700&family=Fira+Sans+Condensed:wght@600&family=Fira+Sans:wght@700&display=swap">
<style>
  :root {
    --blue-deep: #0a2f8c;
    --blue-mid: #1f5fd6;
    --blue-glow: #3f88f0;
    --blue-faint: rgba(10, 40, 120, 0.28);
    --white: #ffffff;
    --suit-dark: #121722;
    --suit-mid: #2b3140;
  }
  html, body {
    margin: 0;
    padding: 0;
    width: 848px;
    height: 1200px;
    overflow: hidden;
    background: #ffffff;
  }
  .poster {
    position: relative;
    width: 848px;
    height: 1200px;
    overflow: hidden;
    background:
      radial-gradient(ellipse 420px 520px at 560px 430px, var(--blue-glow) 0%, var(--blue-mid) 45%, transparent 100%),
      linear-gradient(180deg, var(--blue-deep) 0%, var(--blue-mid) 40%, var(--blue-mid) 70%, var(--blue-deep) 100%);
    color: var(--white);
  }
  .backdrop-words {
    position: absolute;
    inset: 0;
    font-family: "Stardos Stencil", Impact, sans-serif;
    font-weight: 700;
    color: var(--blue-faint);
    font-size: 150px;
    line-height: 120px;
    white-space: nowrap;
    padding-left: 300px;
    pointer-events: none;
  }
  .speaker-photo {
    position: absolute;
    left: 0;
    top: 62px;
    width: 300px;
    height: 1138px;
    border-radius: 140px 140px 0 0;
    background: linear-gradient(180deg, #c79a80 0%, #b88a72 14%, var(--suit-mid) 22%, var(--suit-dark) 100%);
  }
  .header {
    position: absolute;
    left: 320px;
    top: 44px;
    width: 500px;
    text-align: center;
    font-family: "Fira Sans", Arial, sans-serif;
    font-weight: 700;
  }
  .header .doctor {
    font-size: 42px;
    letter-spacing: 22px;
    line-height: 50px;
  }
  .header .label {
    font-size: 21px;
    letter-spacing: 9px;
    line-height: 28px;
    margin-left: -40px;
  }
  .title {
    position: absolute;
    left: 290px;
    top: 135px;
    width: 540px;
    height: 510px;
  }
  .title text {
    font-family: "Stardos Stencil", Impact, sans-serif;
    font-weight: 700;
    fill: var(--white);
  }
  .benefits {
    position: absolute;
    left: 330px;
    top: 655px;
    width: 470px;
    margin: 0;
    padding: 0;
    list-style: none;
    text-align: center;
    font-family: "Fira Sans Condensed", Arial, sans-serif;
    font-weight: 600;
    font-size: 17px;
    line-height: 20px;
    text-transform: uppercase;
  }
  .benefits li { margin-bottom: 22px; }
  .benefits li:last-child { margin-bottom: 0; }
</style>
</head>
<body>
<main class="poster">
  <div class="backdrop-words" aria-hidden="true">
    AND<br>ARMOR PLATING<br>YOUR WELLNESS<br>TOTAL SHAPE<br>RESET<br>TOTAL<br>SHAPE<br>ARMOR<br>RESET<br>WELLNESS
  </div>

  <div class="speaker-photo" role="img" aria-label="Portrait of Dr. Prent in a dark suit, white shirt and pink tie"></div>

  <header class="header">
    <div class="doctor">DR. PRENT'S</div>
    <div class="label">SEMINAR</div>
  </header>

  <svg class="title" viewBox="0 0 540 510" aria-label="Total Shape Reset and Armor Plating your Wellness">
    <text x="15" y="100" font-size="110" textLength="505" lengthAdjust="spacingAndGlyphs">TOTAL</text>
    <text x="15" y="212" font-size="110" textLength="505" lengthAdjust="spacingAndGlyphs">SHAPE</text>
    <text x="15" y="364" font-size="175" textLength="505" lengthAdjust="spacingAndGlyphs">RESET</text>
    <text x="15" y="428" font-size="34" textLength="70" lengthAdjust="spacingAndGlyphs">AND</text>
    <text x="95" y="428" font-size="60" textLength="425" lengthAdjust="spacingAndGlyphs">ARMOR PLATING</text>
    <text x="15" y="496" font-size="66" textLength="505" lengthAdjust="spacingAndGlyphs">YOUR WELLNESS</text>
  </svg>

  <ul class="benefits">
    <li>How to shed pounds and rapidly reduce<br>their waist size</li>
    <li>Why weight loss doesn't work 99.9% of<br>the time so that you can be the successful<br>0.1%</li>
    <li>Expose the lies and reveal the truth about<br>the real causes of heart disease, diabetes,<br>etc., and how to reverse/prevent this</li>
    <li>The insider secrets to building your body<br>into a health fortress unbreachable by<br>sickness and disease</li>
    <li>Learn to live and fufill your God-given<br>health potential</li>
    <li>Eliminate high bloodpressure, high<br>cholesterol, diabetes, fatigue, chronic<br>pain</li>
    <li>Ending the war on sickness and disease by<br>launching an unstoppable health<br>offensive that will pummel any enemy of<br>life and health</li>
  </ul>
</main>
</body>
</html>
```